We are a Yacht Charter Broker servicing VIP clients on booking sailing catamarans and motor yacht...

We are looking for a wildly creative website to attract high net worth clients to work with us in booking their dream yacht vacation. A site that you think is 5 years ahead of its time. Sexy, modern and unique. Our company name is BRELLAVON. Our colors are navy blue and silver.
BLUE:
RGBB 0/44/92
CMYC 100/86/36/31
SILVER:
RGB 152/163/173
CMYK 43/29/25/0

HEX 98a3ad

Target Market(s)

High net worth people in need of white glove brokerage serving in finding and booking their dream yacht for a vacation of a lifetime.

Coding

Coded - Design and coding required

Number of Pages Required

1 page

Requirements
Must have
• Mobile friendly.
• Wildly creative and different. A website that we would expect to see 5 years from now.
• Pictures of yachts and or people on yachts. Palm tree landscapes.
• pictures of high end food related to the VIP yacht experience.
Nice to have
• Anything you feel would sell the yacht charter experience.
Should not have
• Nothing comes to mind.

```html
<!DOCTYPE html>
<html lang="en">
<head>
<meta charset="UTF-8">
<title>BRELLAVON — Yacht Charter</title>
<link href="https://fonts.googleapis.com/css2?family=Raleway:wght@200;300;400&display=swap" rel="stylesheet">
<style>
  :root {
    --navy: #00008a;
    --navy-deep: #1b2a4e;
    --white: #ffffff;
    --silver: #d8dde4;
    --sky: #2f78c8;
    --palm: #7bb33a;
    --tint: rgba(60, 120, 190, 0.55);
  }
  * { margin: 0; padding: 0; box-sizing: border-box; }
  html, body {
    width: 1200px; height: 750px; overflow: hidden;
    background: var(--white);
    font-family: "Raleway", sans-serif;
  }
  .site { position: relative; width: 1200px; height: 750px; overflow: hidden; }
  .topbar {
    position: absolute; left: 0; top: 0; width: 1200px; height: 60px;
    background: var(--navy);
  }
  .topbar__nav { display: flex; position: absolute; left: 70px; top: 15px; gap: 0; }
  .topbar__link {
    color: var(--white); text-decoration: none; font-weight: 300;
    font-size: 19px; letter-spacing: 0.3px; margin-right: 38px;
    position: relative;
  }
  .topbar__link--active::after {
    content: ""; position: absolute; left: 50%; top: 37px;
    transform: translateX(-50%);
    border-left: 5px solid transparent; border-right: 5px solid transparent;
    border-bottom: 5px solid var(--white);
  }
  .hero { position: absolute; left: 0; top: 60px; width: 1200px; height: 588px; }
  .hero__art { position: absolute; inset: 0; }
  .hero__title {
    position: absolute; left: 50px; top: 2px;
    font-weight: 200; font-size: 70px; letter-spacing: 1px;
    color: var(--silver); opacity: 0.9;
  }
  .hero__cursor {
    position: absolute; left: 53px; top: 80px; width: 1px; height: 15px;
    background: var(--white);
  }
  .brand {
    position: absolute; left: 0; width: 1200px; top: 688px;
    text-align: center; font-weight: 400; font-size: 62px;
    letter-spacing: 14px; color: var(--navy-deep);
  }
</style>
</head>
<body>
<div class="site">
  <header class="topbar">
    <nav class="topbar__nav">
      <a class="topbar__link topbar__link--active" href="#">Home</a>
      <a class="topbar__link" href="#">Contact</a>
      <a class="topbar__link" href="#">Destinations</a>
      <a class="topbar__link" href="#">Fine Dining</a>
    </nav>
  </header>

  <section class="hero">
    <svg class="hero__art" width="1200" height="588" viewBox="0 0 1200 588">
      <defs>
        <linearGradient id="palmSky" x1="0" y1="0" x2="1" y2="1">
          <stop offset="0" stop-color="#8cc43e"/>
          <stop offset="0.35" stop-color="#4f8a3a"/>
          <stop offset="0.6" stop-color="#2f74c6"/>
          <stop offset="1" stop-color="#b9cde6"/>
        </linearGradient>
      </defs>
      <rect role="img" aria-label="Photo of palm trees against a blue sky with white clouds" x="0" y="0" width="1200" height="588" fill="url(#palmSky)"/>
      <path class="hero__tint" d="M704,0 C900,40 1080,150 1124,292 Q1170,140 1200,0 Z" fill="var(--tint)"/>
      <path class="hero__navy" d="M640,588 C880,560 1060,440 1124,292 Q1180,430 1200,588 Z" fill="var(--navy)"/>
      <path class="hero__crescent" d="M1200,0 Q1170,170 1124,292 Q1182,430 1200,588 Z" fill="var(--white)"/>
      <path class="hero__edge" d="M704,0 C900,40 1080,150 1124,292 C1060,440 880,560 640,588" fill="none" stroke="rgba(255,255,255,0.5)" stroke-width="1.5"/>
    </svg>
    <h1 class="hero__title">BRELLAVON</h1>
    <span class="hero__cursor"></span>
  </section>

  <div class="brand">BRELLAVON</div>
</div>
</body>
</html>
```